Original Cellphone and Tablet Accesories

We are Morvet SAS, we sell the biggest brands in cell phone accesories like Kelvora, Brindlecase, Talvok, Wenzo, Duskmantle, Hardweld, PFX, Varuno,Glint, Volmer and we are about to release our trellix ecommerce.

We would like to see website designs according to our corporate image (file attached)

User needs to be able to search by Cell phone(device), like Pelora 7T, by Brand, like Brindlecase and by Category like Cases. We need responsive and revolutionary design, this is the most important part for catch client in our site.

We Like lastest device design (2)

We like Top menus with pic (1)

Home should have:

Best Sellers
Lastest Devices
Lastest Arrivals
Space for our phone line

The product page has to have tabs for:
Compatibility
Specs

And this item on product page:
Email alerts: price drop, back in stock

We like 1 page checkout, but open to see new proposals (4)*
*This is very important, this is where clients buys or leaves site... I need big proposals here

We like big side to side banners (3)

We wants the cleanest design possible.

We want to transmit confidence, most this market here in Colombia is counterfeit products, so we want to transmit that we sell original brand products.

Attached file sent in spanish (clasificaciones y filtros) categories and filters, I hope this helps you for design.

Brands we sell reference sites:

www.varuno-shop.example
www.brindlecase.example
www.talvok.example
http://www.kelvora.example/africa_en/consumer/mobile-phone/mobile-phone/mobile-phone-accessories/
http://store.wenzo.example/

Like design:

www.gadgetrove.example

These are the market leaders world wide, don't like his design, but do like some or their filters and features:

http://www.handsetbarn.example/

Reference lastest devices:

Quorra Pelora 7t
Kelvora Zenith Pad 3
Kelvora Zenith K4
Wenzo Lumio R1
Wenzo Lumio R Maxima
Quorra Slate Breeze
BRV Uno
DK T2
DK Vertex 5
Updates

Please focus on usability interface:
search by

device> category> brand
brand>device

the goal is the client get to the products they are looking for the easier way and see related items to get more sales.

Target Market(s)

Early adopters on new cell phone and tablet devices aged at 20-60, they likes to show off their new acquisition

Industry/Entity Type

Cell Phone

Colors
33a6d7
33a7d8
cee9f6
ffffff
ebf7f9
d9eff7

Requirements
Must have
• a design to filter by cell phone device, brand or category

website should communicate we sell original cell phone accessories, not counterfeit products

website should communicate we sell quality products

```html
<!DOCTYPE html>
<html lang="en">
<head>
<meta charset="utf-8">
<title>Morvet — Original Phone &amp; Tablet Accessories</title>
<link href="https://fonts.googleapis.com/css2?family=Open+Sans:wght@400;600;700&family=Montserrat:wght@400;600;700&display=swap" rel="stylesheet">
<style>
:root{
  --blue:#33a6d7;
  --blue-dark:#2a8fbb;
  --blue-pale:#cee9f6;
  --blue-mist:#ebf7f9;
  --blue-soft:#d9eff7;
  --white:#ffffff;
  --ink:#2b2b2b;
  --charcoal:#333333;
  --nav:#2e2e2e;
  --grey:#f0f0f0;
  --grey-line:#dddddd;
  --muted:#888888;
  --green:#8cc63f;
  --star:#f5a623;
  --price:#33a6d7;
}
*{box-sizing:border-box;margin:0;padding:0}
html,body{width:1200px;height:2748px;overflow:hidden}
body{background:var(--white);font-family:"Open Sans",Arial,sans-serif;color:var(--ink);font-size:12px;position:relative}
.wrap{width:960px;margin:0 auto;position:relative}
a{color:inherit;text-decoration:none}

/* header */
.site-header{height:262px;position:relative}
.account-links{position:absolute;right:120px;top:0;height:26px;background:var(--nav);color:#fff;display:flex;gap:22px;align-items:center;padding:0 18px;font-size:11px}
.account-links span::before{content:"";display:inline-block;width:8px;height:8px;background:#fff;border-radius:2px;margin-right:6px;vertical-align:-1px}
.brand{position:absolute;left:120px;top:48px;display:flex;align-items:center;gap:14px}
.brand-dot{width:44px;height:44px;border-radius:50%;background:var(--blue)}
.brand-name{font-family:"Montserrat",sans-serif;font-weight:600;font-size:46px;color:var(--charcoal);letter-spacing:2px}
.phone-line{position:absolute;right:120px;top:104px;display:flex;align-items:center;gap:8px;font-family:"Montserrat",sans-serif;font-size:22px;color:var(--blue)}
.phone-line svg{width:30px;height:30px}
.search-row{position:absolute;left:120px;top:212px;height:40px;display:flex;border:2px solid var(--blue);border-radius:3px;overflow:hidden;width:640px}
.search-cat{width:150px;background:var(--grey);display:flex;align-items:center;padding:0 12px;font-weight:600;font-size:12px;justify-content:space-between;border-right:1px solid var(--grey-line)}
.search-input{flex:1;display:flex;align-items:center;padding:0 14px;color:var(--muted)}
.search-btn{width:46px;background:var(--blue);display:flex;align-items:center;justify-content:center}

/* nav */
.main-nav{height:38px;background:var(--nav);border-bottom:3px solid var(--blue)}
.main-nav ul{list-style:none;display:flex;height:35px;width:960px;margin:0 auto}
.main-nav li{color:#fff;font-family:"Montserrat",sans-serif;font-size:12px;font-weight:600;padding:0 18px;display:flex;align-items:center;border-right:1px solid #444}
.main-nav li.home{background:var(--blue);padding:0 14px}

/* hero */
.hero{height:400px;background:var(--grey)}
.hero .wrap{height:400px}
.hero-copy{position:absolute;left:0;top:96px;width:330px}
.hero-kicker{font-family:"Montserrat",sans-serif;color:var(--blue);font-size:22px}
.hero-title{font-family:"Montserrat",sans-serif;color:var(--blue);font-size:25px;font-weight:600;line-height:1.15;white-space:nowrap}
.hero-sub{font-family:"Montserrat",sans-serif;color:var(--muted);font-size:18px;margin:4px 0 10px}
.hero-copy p{font-size:11px;color:#555;line-height:1.5;width:300px}
.btn-dark{display:inline-block;margin-top:16px;background:var(--charcoal);color:#fff;padding:9px 16px;font-size:11px;border-radius:2px}
.hero-devices{position:absolute;left:350px;top:64px;width:340px;height:270px;background:linear-gradient(135deg,#e6e6e6,#bdbdbd 55%,#f7f7f7);border-radius:6px}
.finder{position:absolute;right:0;top:40px;width:230px;height:300px;background:#3a3a3a}
.finder h3{background:var(--blue);color:#fff;text-align:center;font-family:"Montserrat",sans-serif;font-size:15px;padding:10px 0;letter-spacing:1px}
.finder .select{margin:16px 16px 0;height:30px;background:#fff;border-radius:2px;display:flex;align-items:center;justify-content:space-between;padding:0 10px;color:#666;font-size:11px}
.finder .select::after{content:"";border:4px solid transparent;border-top-color:#666;margin-top:4px}
.btn-find{display:block;width:60px;margin:30px auto 0;background:var(--green);color:#fff;font-weight:700;text-align:center;padding:8px 0;font-size:11px}

/* section bars */
.bar{height:36px;background:var(--charcoal);display:flex;align-items:center;color:#fff;font-family:"Montserrat",sans-serif;font-weight:600;font-size:12px;letter-spacing:.5px}
.bar .tag{width:36px;height:36px;background:var(--blue);margin-right:14px;display:flex;align-items:center;justify-content:center}
.bar.plain{padding-left:14px}
.bar.blue{background:var(--blue)}
.bar .pager{margin-left:auto;margin-right:10px;display:flex;gap:6px}
.bar .pager i{width:16px;height:16px;border-radius:50%;background:#666;display:block}

.latest-devices{margin-top:72px}
.device-row{display:flex;justify-content:space-between;padding:22px 8px 0}
.device{width:200px;position:relative}
.ribbon{position:absolute;left:6px;top:-22px;width:26px;height:44px;background:var(--green);color:#fff;font-size:8px;font-weight:700;text-align:center;padding-top:12px;clip-path:polygon(0 0,100% 0,100% 100%,50% 82%,0 100%)}
.device-pic{width:90px;height:170px;margin:0 auto;border-radius:10px;background:linear-gradient(160deg,#555,#111)}
.device h4{font-size:10px;font-weight:600;margin-top:14px;color:#444}
.device .meta{display:flex;justify-content:space-between;margin-top:6px;font-size:11px}
.price{color:var(--price);font-weight:700}
.old{color:var(--muted);text-decoration:line-through;margin-right:4px;font-weight:400}
.stars{color:var(--star);letter-spacing:1px}

.latest-arrivals{margin-top:32px}
.arrival-row{display:flex;justify-content:space-between;align-items:center;background:var(--grey);padding:0 20px;height:340px}
.card{width:160px;background:#fff;border:1px solid var(--grey-line);padding:14px 12px;text-align:left}
.card .pic{width:60px;height:110px;margin:0 auto 12px;border-radius:6px;background:linear-gradient(160deg,#4a4a4a,#0f0f0f)}
.arrival-row .card .pic{height:130px;width:68px}
.card h5{font-size:10px;font-weight:600;color:#444}
.card .price{display:block;margin-top:4px;font-size:11px}

.split{display:flex;justify-content:space-between;margin-top:100px}
.by-brand{width:560px}
.brand-row{display:flex;justify-content:space-between;background:var(--grey);padding:24px 16px;height:262px}
.brand-row .card{width:120px}
.best{width:368px}
.best-body{background:var(--grey);height:262px;padding:14px 16px;position:relative}
.best-pager{display:flex;justify-content:flex-end;gap:4px;margin-bottom:10px}
.best-pager span{width:18px;height:18px;border:1px solid var(--grey-line);background:#fff;font-size:10px;display:flex;align-items:center;justify-content:center}
.best-pager span.on{background:var(--blue);color:#fff;border-color:var(--blue)}
.best-items{display:flex;gap:14px}
.best-item{flex:1;background:#fff;border:1px solid var(--grey-line);padding:14px;position:relative}
.best-item .new{position:absolute;right:-8px;top:-10px;width:34px;height:34px;border-radius:50%;background:var(--green);color:#fff;font-size:9px;font-weight:700;display:flex;align-items:center;justify-content:center}
.best-item .pic{width:70px;height:100px;margin:0 auto 10px;border-radius:6px;background:linear-gradient(160deg,#cfd8dc,#6d7b82)}
.best-item h5{font-size:11px;font-weight:600;text-align:center}
.best-item .btn-spec{display:block;margin-top:10px;background:var(--charcoal);color:#fff;text-align:center;font-size:9px;padding:6px 0}

.promo-row{display:flex;justify-content:space-between;margin-top:82px}
.promo{width:560px;height:300px;background:var(--blue-mist);position:relative;overflow:hidden;border:1px solid var(--blue-soft)}
.promo-copy{position:absolute;left:24px;top:28px;width:250px}
.promo-copy h2{font-family:"Montserrat",sans-serif;font-size:24px;font-weight:600;color:var(--charcoal);line-height:1.15}
.promo-copy .offer{font-family:"Montserrat",sans-serif;font-size:14px;color:var(--charcoal);margin-top:6px}
.promo-copy .url{color:var(--blue);font-size:11px;margin-top:2px}
.btn-blue{display:inline-block;background:var(--blue);color:#fff;font-size:11px;font-weight:700;padding:8px 16px;margin-top:14px}
.promo-brands{position:absolute;left:24px;bottom:22px;display:flex;gap:16px;font-size:11px;font-weight:700;color:var(--charcoal)}
.promo-cases{position:absolute;right:30px;top:20px;width:220px;height:260px;background:linear-gradient(120deg,#d9c6a8,#9aa4ab 45%,#f0f0f0);border-radius:8px}
.feeds{width:368px}
.feeds h3{font-family:"Montserrat",sans-serif;font-size:14px;font-weight:700;padding:6px 0 14px;border-bottom:1px solid var(--grey-line)}
.tweet{display:flex;gap:12px;padding:16px 0;border-bottom:1px solid var(--grey-line);font-size:11px;color:#555;line-height:1.5}
.tweet i{flex:none;width:22px;height:22px;border-radius:50%;background:var(--blue)}
.tweet b{color:var(--blue);font-weight:600}

.our-brands{margin-top:110px}
.our-brands h3{font-family:"Montserrat",sans-serif;font-size:14px;font-weight:700}
.brand-strip{display:flex;justify-content:space-between;align-items:center;margin-top:24px;padding:0 10px;height:50px}
.brand-strip span{font-family:"Open Sans",sans-serif;font-size:22px;font-weight:700;color:var(--charcoal)}

.site-footer{position:absolute;left:0;top:2490px;width:1200px;height:226px;background:var(--grey);border-top:1px solid var(--grey-line)}
.footer-cols{display:flex;justify-content:space-between;padding-top:30px}
.footer-cols div{width:170px}
.footer-cols h6{color:var(--blue);font-size:10px;font-weight:700;letter-spacing:.5px;margin-bottom:10px}
.footer-cols p{font-size:10px;color:#666;line-height:1.9}
.bottom-strip{position:absolute;left:0;top:2716px;width:1200px;height:32px;background:var(--nav);color:#aaa;font-size:10px}
.bottom-strip .wrap{display:flex;justify-content:space-between;align-items:center;height:32px}
.social{display:flex;gap:6px}
.social i{width:18px;height:18px;border-radius:50%;background:#555;display:block}
</style>
</head>
<body>

<header class="site-header">
  <nav class="account-links"><span>Log In</span><span>My Wishlist</span><span>My Account</span><span>My Cart (0 items)</span><span>Checkout</span></nav>
  <div class="brand"><span class="brand-dot"></span><span class="brand-name">MORVET</span></div>
  <div class="phone-line">
    <svg viewBox="0 0 24 24"><circle cx="12" cy="12" r="11" fill="none" stroke="#33a6d7" stroke-width="2"/><path d="M8 6l2 0 1 3-1.5 1a7 7 0 0 0 3.5 3.5L14 12l3 1v2a2 2 0 0 1-2 2A9 9 0 0 1 6 8a2 2 0 0 1 2-2z" fill="#33a6d7"/></svg>
    <span>Call: 555-014-2290</span>
  </div>
  <div class="search-row">
    <div class="search-cat">All Categories <svg width="8" height="6"><path d="M0 0h8L4 6z" fill="#555"/></svg></div>
    <div class="search-input">Search entire store here...</div>
    <div class="search-btn"><svg width="18" height="18" viewBox="0 0 18 18"><circle cx="7.5" cy="7.5" r="5.5" fill="none" stroke="#fff" stroke-width="2"/><path d="M12 12l5 5" stroke="#fff" stroke-width="2"/></svg></div>
  </div>
</header>

<nav class="main-nav">
  <ul>
    <li class="home"><svg width="14" height="14" viewBox="0 0 14 14"><path d="M1 7L7 1l6 6h-2v6H9V9H5v4H3V7z" fill="#fff"/></svg></li>
    <li>SMARTPHONES</li><li>COMPUTER &amp; TABLETS</li><li>BRANDS</li><li>ACCESSORIES</li><li>SUPPORT</li><li>ABOUT</li><li>CONTACT</li>
  </ul>
</nav>

<section class="hero">
  <div class="wrap">
    <div class="hero-copy">
      <div class="hero-kicker">New Season</div>
      <div class="hero-title">Smart Phones Tablets</div>
      <div class="hero-sub">Original and Certified</div>
      <p>Lorem ipsum dolor sit amet, consectetur adipisicing elit, sed do eiusmod tempor incididunt ut labore et dolore magna aliqua.</p>
      <a class="btn-dark">Discover More Devices</a>
    </div>
    <div class="hero-devices" role="img" aria-label="Group of smartphones and tablets on display"></div>
    <aside class="finder">
      <h3>SEARCH</h3>
      <div class="select">Select Category</div>
      <div class="select">Select Make</div>
      <div class="select">Select Model</div>
      <a class="btn-find">FIND</a>
    </aside>
  </div>
</section>

<section class="wrap latest-devices">
  <div class="bar"><span class="tag"><svg width="14" height="14"><path d="M7 1l1.8 4 4.2.4-3.2 2.8 1 4.3L7 10.3 3.2 12.5l1-4.3L1 5.4 5.2 5z" fill="#fff"/></svg></span>LATEST DEVICES<span class="pager"><i></i><i></i></span></div>
  <div class="device-row">
    <article class="device"><span class="ribbon">SALE</span><div class="device-pic" role="img" aria-label="Black smartphone front view"></div><h4>SLIM GUARD ZENITH</h4><div class="meta"><span class="price"><span class="old">$500.00</span>$450.00</span><span class="stars">★★★★★</span></div></article>
    <article class="device"><span class="ribbon">SALE</span><div class="device-pic" role="img" aria-label="Dark smartphone front view"></div><h4>FLIP SHELL LUMIO</h4><div class="meta"><span class="price">$450.00</span><span class="stars">★★★★★</span></div></article>
    <article class="device"><span class="ribbon">SALE</span><div class="device-pic" role="img" aria-label="Black smartphone front view"></div><h4>PRO DOCK VERTEX</h4><div class="meta"><span class="price">$450.00</span><span class="stars">★★★★★</span></div></article>
    <article class="device"><span class="ribbon">SALE</span><div class="device-pic" role="img" aria-label="Smartphone front view"></div><h4>PRO DOCK PELORA</h4><div class="meta"><span class="price">$450.00</span><span class="stars">★★★★★</span></div></article>
  </div>
</section>

<section class="wrap latest-arrivals">
  <div class="bar plain">LATEST ARRIVALS</div>
  <div class="arrival-row">
    <article class="card"><div class="pic" role="img" aria-label="Smartphone product photo"></div><h5>ARMOR CASE SLIM</h5><span class="price"><span class="old">$150</span>$120.00</span></article>
    <article class="card"><div class="pic" role="img" aria-label="Smartphone product photo"></div><h5>ARMOR CASE SLIM</h5><span class="price"><span class="old">$150</span>$120.00</span></article>
    <article class="card"><div class="pic" role="img" aria-label="Smartphone product photo"></div><h5>ARMOR CASE SLIM</h5><span class="price"><span class="old">$150</span>$120.00</span></article>
    <article class="card"><div class="pic" role="img" aria-label="Smartphone product photo"></div><h5>ARMOR CASE SLIM</h5><span class="price"><span class="old">$150</span>$120.00</span></article>
    <article class="card"><div class="pic" role="img" aria-label="Smartphone product photo"></div><h5>ARMOR CASE SLIM</h5><span class="price"><span class="old">$150</span>$120.00</span></article>
  </div>
</section>

<section class="wrap split">
  <div class="by-brand">
    <div class="bar plain">PRODUCTS BY BRAND</div>
    <div class="brand-row">
      <article class="card"><div class="pic" role="img" aria-label="Smartphone product photo"></div><h5>ARMOR CASE SLIM</h5><span class="price">$120.00</span></article>
      <article class="card"><div class="pic" role="img" aria-label="Smartphone product photo"></div><h5>ARMOR CASE SLIM</h5><span class="price">$120.00</span></article>
      <article class="card"><div class="pic" role="img" aria-label="Smartphone product photo"></div><h5>ARMOR CASE SLIM</h5><span class="price">$120.00</span></article>
      <article class="card"><div class="pic" role="img" aria-label="Smartphone product photo"></div><h5>ARMOR CASE SLIM</h5><span class="price">$120.00</span></article>
    </div>
  </div>
  <div class="best">
    <div class="bar blue plain">BEST ARRIVALS</div>
    <div class="best-body">
      <div class="best-pager"><span>‹</span><span class="on">1</span><span>2</span><span>›</span></div>
      <div class="best-items">
        <article class="best-item"><span class="new">NEW</span><div class="pic" role="img" aria-label="Large-screen phone product photo"></div><h5>Zenith Pad II</h5><a class="btn-spec">Read Specification</a></article>
        <article class="best-item"><span class="new">NEW</span><div class="pic" role="img" aria-label="Large-screen phone product photo"></div><h5>Zenith Pad II</h5><a class="btn-spec">Read Specification</a></article>
      </div>
    </div>
  </div>
</section>

<section class="wrap promo-row">
  <div class="promo">
    <div class="promo-copy">
      <h2>LATEST PELORA 7T CASES</h2>
      <div class="offer">SPECIAL OFFER AT</div>
      <div class="url">morvet.example</div>
      <a class="btn-blue">SHOP NOW</a>
    </div>
    <div class="promo-brands"><span>Brindlecase</span><span>Talvok</span><span>Varuno</span><span>Glint</span></div>
    <div class="promo-cases" role="img" aria-label="Row of colourful protective phone cases"></div>
  </div>
  <aside class="feeds">
    <h3>CHIRPLINE FEEDS</h3>
    <div class="tweet"><i></i><p>New arrivals this week, another fitted phone case now listed on the store <b>#morvetdeals</b></p></div>
    <div class="tweet"><i></i><p>New arrivals this week, another fitted phone case now listed on the store <b>#morvetdeals</b></p></div>
    <div class="tweet"><i></i><p>New arrivals this week, another fitted phone case now listed on the store <b>#morvetdeals</b></p></div>
  </aside>
</section>

<section class="wrap our-brands">
  <h3>OUR BRANDS</h3>
  <div class="brand-strip"><span>KELVORA</span><span>VOLMER</span><span>KORVIK</span><span>BRINDLECASE</span><span>SHELLWISE</span><span>REDMARK</span></div>
</section>

<footer class="site-footer">
  <div class="wrap footer-cols">
    <div><h6>INFORMATION</h6><p>About Us<br>Delivery Information<br>Privacy Policy<br>Terms &amp; Conditions</p></div>
    <div><h6>CUSTOMER SERVICE</h6><p>Contact Us<br>Returns<br>Site Map</p></div>
    <div><h6>EXTRAS</h6><p>Brands<br>Gift Vouchers<br>Affiliates<br>Specials</p></div>
    <div><h6>MY ACCOUNT</h6><p>My Account<br>Order History<br>Wish List<br>Newsletter</p></div>
    <div><h6>ONLINE SUPPORT</h6><p>Sales: 555-014-2290<br>Help: 555-014-2291</p></div>
  </div>
</footer>
<div class="bottom-strip">
  <div class="wrap"><span>© Morvet SAS. All rights reserved.</span><span class="social"><i></i><i></i><i></i><i></i></span></div>
</div>

</body>
</html>
```